Invitation Card for Marketing and Warehouse Invitation

I am looking Innovative and attractive Invitation card. Please visit my facebook page www.pelvantu.example/trivasko

What I want to show residents of Verdant Town Lahore.

1. Order delivery in 21 minutes. Fastest delivery in the WORLD.
2. We are Opening our OWN WareHouse on 22nd September
3. you are invited
4. All products and stuff HIGH quality then Verdant Town Local Market
5. More discount than local market
6. We provide everything

Note: Please visit my fb page and get more details for services and Ideal. Now you need to decide that it should be a two-way card or a single page. I want to invite to residents of Verdant Town and same way marketing as well. Please also watch one of the videos on the facebook and see the last page the more details which need to come as well like phone numbers and social media links. Please get logo from facebook page.

Target Market(s)

Residents of Verdant Town Lahore Pakistan about 15K residents/House

Industry/Entity Type

Marketing

Font styles to use
Serif

Colors

Designer to choose colors to be used in the design.

Requirements
Must have
• Warehouse opening on 22/09
• High-Quality grocery/Vegetable and fruits
• Cheaper than local market
• First Warehouse in Pakistan
Nice to have
• Please check facebook page for this and get more idea
Should not have
• Copy/Paste Idea

```html
<!DOCTYPE html>
<html lang="en">
<head>
<meta charset="utf-8">
<title>Warehouse Invitation Card</title>
<link rel="stylesheet" href="https://fonts.googleapis.com/css2?family=Cinzel:wght@700;800&family=Open+Sans:wght@400;600&display=swap">
<style>
  :root {
    --page-bg: #262626;
    --header-green: #3a9b1b;
    --header-green-dark: #2c8a10;
    --header-green-light: #55b02e;
    --band-brown: #6b5548;
    --text-brown: #5b4638;
    --accent-green: #2f9a12;
    --body-top: #e6ee9c;
    --body-bottom: #f2f1ae;
    --body-text: #4a3b30;
    --white: #ffffff;
  }
  * { margin: 0; padding: 0; box-sizing: border-box; }
  html, body { width: 1200px; height: 960px; overflow: hidden; }
  body { background: var(--page-bg); position: relative; font-family: "Open Sans", sans-serif; }

  .card {
    position: absolute; left: 0; top: 52px; width: 1200px; height: 856px;
    background: linear-gradient(180deg, var(--body-top) 0%, #eef3a6 55%, var(--body-bottom) 100%);
    overflow: hidden;
  }
  .header-band { position: absolute; left: 0; top: 0; width: 1200px; height: 290px; }

  .headline {
    position: absolute; left: 0; width: 100%; text-align: center; white-space: nowrap;
    font-family: "Cinzel", serif; font-weight: 800; color: var(--white); line-height: 1;
  }
  .headline--invite { top: 20px; font-size: 100px; }
  .headline--place  { top: 114px; font-size: 64px; }
  .headline--date   { top: 180px; font-size: 74px; }
  .headline--date .sup { font-size: 36px; vertical-align: 32px; }

  .claim {
    position: absolute; top: 306px; left: 0; width: 100%; text-align: center; white-space: nowrap;
    font-family: "Cinzel", serif; font-weight: 800; font-size: 56px; line-height: 1.2; color: var(--text-brown);
  }
  .claim .country { color: var(--accent-green); }

  .feature { position: absolute; top: 376px; display: flex; align-items: flex-start; }
  .feature__icon { width: 78px; height: 78px; flex: none; }
  .feature__text {
    font-size: 21px; line-height: 26px; color: var(--body-text); margin-left: 30px; margin-top: 14px;
  }
  .feature--quality { left: 48px; }
  .feature--discount { left: 476px; }
  .feature--range { left: 826px; }
  .feature--range .feature__text { margin-top: 16px; }

  .contact-title {
    position: absolute; left: 68px; top: 490px; font-family: "Cinzel", serif; font-weight: 800;
    font-size: 28px; line-height: 1.2; color: var(--text-brown); white-space: nowrap;
    padding-bottom: 4px; border-bottom: 2px solid var(--text-brown);
  }
  .contact-line { position: absolute; display: flex; align-items: flex-start; color: var(--body-text); white-space: nowrap; }
  .contact-line svg { flex: none; margin-right: 18px; }
  .contact-line--address { left: 66px; top: 551px; font-size: 21px; line-height: 25px; }
  .contact-line--address svg { margin-top: 6px; }
  .contact-line--phone { left: 708px; top: 549px; font-size: 24px; font-weight: 600; }
  .contact-line--phone svg { margin-top: 8px; }
  .contact-line--web { left: 708px; top: 584px; font-size: 21px; }
  .contact-line--web svg { margin-top: 7px; }

  .produce-strip {
    position: absolute; left: 0; top: 612px; width: 1200px; height: 244px;
    background: linear-gradient(180deg, rgba(90,150,50,0) 0%, #6fa53a 22%, #5b8f2a 45%, #a7783f 70%, #8c5a2c 100%);
  }
  .brand-badge {
    position: absolute; left: 934px; top: 658px; width: 270px; height: 270px;
    border-radius: 50%; background: var(--white);
  }
  .brand-badge__name {
    position: absolute; left: 0; top: 92px; width: 100%; text-align: center;
    font-size: 32px; font-weight: 400; color: var(--accent-green);
  }
</style>
</head>
<body>
<main class="card">
  <svg class="header-band" viewBox="0 0 1200 290" aria-hidden="true">
    <defs>
      <linearGradient id="headerFill" x1="0" y1="0" x2="0" y2="1">
        <stop offset="0" stop-color="var(--header-green-dark)"/>
        <stop offset="1" stop-color="var(--header-green)"/>
      </linearGradient>
    </defs>
    <path d="M0 0 H1200 V199 Q640 340 0 222 Z" fill="var(--band-brown)"/>
    <path d="M0 0 H1200 V190 Q640 326 0 214 Z" fill="url(#headerFill)"/>
    <path d="M0 220 Q600 120 1200 196 Q640 322 0 220 Z" fill="var(--header-green-light)" opacity="0.55"/>
  </svg>

  <h1 class="headline headline--invite">Inviting you</h1>
  <p class="headline headline--place">To our OWN WareHouse</p>
  <p class="headline headline--date">on 22<span class="sup">nd</span> September</p>

  <h2 class="claim">1st Warehouse in <span class="country">Pakistan</span></h2>

  <div class="feature feature--quality">
    <svg class="feature__icon" viewBox="0 0 78 78" aria-hidden="true">
      <circle cx="39" cy="39" r="36" fill="none" stroke="var(--text-brown)" stroke-width="3"/>
      <rect x="20" y="36" width="9" height="20" rx="2" fill="var(--accent-green)" stroke="var(--text-brown)" stroke-width="2"/>
      <path d="M31 37 L38 22 Q42 18 43 24 L41 34 H54 Q58 35 57 40 L54 53 Q53 56 49 56 H31 Z" fill="var(--accent-green)" stroke="var(--text-brown)" stroke-width="2" stroke-linejoin="round"/>
    </svg>
    <p class="feature__text">All products and stuff HIGH<br>quality then Verdant Town<br>Local Market</p>
  </div>

  <div class="feature feature--discount">
    <svg class="feature__icon" viewBox="0 0 78 78" aria-hidden="true">
      <path d="M39 4 L46 10 L55 7 L58 16 L67 19 L65 28 L72 35 L66 42 L69 51 L60 55 L58 64 L49 63 L42 70 L35 64 L26 67 L22 58 L13 55 L15 46 L8 39 L14 32 L11 23 L20 19 L23 10 L32 12 Z" fill="none" stroke="var(--text-brown)" stroke-width="3" stroke-linejoin="round"/>
      <text x="39" y="50" text-anchor="middle" font-family="Open Sans, sans-serif" font-weight="600" font-size="34" fill="var(--accent-green)">%</text>
    </svg>
    <p class="feature__text">More discount than<br>local market</p>
  </div>

  <div class="feature feature--range">
    <svg class="feature__icon" viewBox="0 0 78 78" aria-hidden="true">
      <circle cx="39" cy="39" r="36" fill="none" stroke="var(--text-brown)" stroke-width="3"/>
      <path d="M18 50 Q26 44 34 48 H44 Q47 49 44 52 H35 M44 52 L56 45 Q60 44 58 48 L46 58 H26 L20 56" fill="none" stroke="var(--text-brown)" stroke-width="2.5" stroke-linecap="round" stroke-linejoin="round"/>
      <rect x="33" y="22" width="6" height="6" fill="none" stroke="var(--accent-green)" stroke-width="2"/>
      <circle cx="46" cy="26" r="3" fill="none" stroke="var(--accent-green)" stroke-width="2"/>
      <circle cx="38" cy="36" r="3" fill="none" stroke="var(--text-brown)" stroke-width="2"/>
      <rect x="44" y="33" width="6" height="6" fill="none" stroke="var(--accent-green)" stroke-width="2"/>
    </svg>
    <p class="feature__text">We provide everything</p>
  </div>

  <h3 class="contact-title">Get in touch with us!</h3>

  <p class="contact-line contact-line--address">
    <svg width="14" height="18" viewBox="0 0 14 18" aria-hidden="true"><path d="M7 0 A7 7 0 0 1 14 7 C14 12 7 18 7 18 C7 18 0 12 0 7 A7 7 0 0 1 7 0 Z" fill="var(--body-text)"/><circle cx="7" cy="7" r="2.6" fill="var(--body-top)"/></svg>
    <span>Plot 118-D, 2nd Floor, Sector 'F' Commercial Lily Block,<br>Verdant Town, Lahore</span>
  </p>
  <p class="contact-line contact-line--phone">
    <svg width="18" height="16" viewBox="0 0 18 16" aria-hidden="true"><path d="M1 5 Q9 -1 17 5 L15 8 L12 6 V4 Q9 3 6 4 V6 L3 8 Z" fill="#222"/><rect x="3" y="9" width="12" height="7" rx="1" fill="#222"/></svg>
    <span>0300-5550142 or 042-35550198</span>
  </p>
  <p class="contact-line contact-line--web">
    <svg width="16" height="16" viewBox="0 0 16 16" aria-hidden="true"><circle cx="8" cy="8" r="6.5" fill="none" stroke="#333" stroke-width="1.5"/><path d="M1.5 8 H14.5 M8 1.5 Q4 8 8 14.5 Q12 8 8 1.5" fill="none" stroke="#333" stroke-width="1.2"/></svg>
    <span>www.trivasko.example</span>
  </p>

  <div class="produce-strip" role="img" aria-label="Photo of fresh vegetables, a wicker basket of tomatoes, pasta, spices and jars of olives and pickles"></div>

  <div class="brand-badge">
    <p class="brand-badge__name">Trivasko</p>
  </div>
</main>
</body>
</html>
```